R & T Summit Construction Business Card ideas

We want a business card to represents our company in a way that looks professional but is also a business card that is unique!

Industry/Entity Type

Construction Company

Contact Information for Business Card

open to all design ideas, just want to be able to see different options to choose from in either color or grayscale.

Requirements
Must have
• Our names and phone numbers
• Nolan Pritchett 512-804-2271
• Curtis Hale 512-693-1804
• Business logo

```html
<!DOCTYPE html>
<html lang="en">
<head>
<meta charset="utf-8">
<title>R &amp; T Summit Construction — Business Card</title>
<link rel="stylesheet" href="https://fonts.googleapis.com/css2?family=Cinzel:wght@600&family=EB+Garamond:wght@400&display=swap">
<style>
  :root {
    --backdrop: #e9e6e1;
    --card: #ffffff;
    --ink: #141414;
    --phone: #6e6e6e;
    --rule: #c9c9c9;
  }
  html, body {
    margin: 0;
    padding: 0;
    width: 1200px;
    height: 987px;
    overflow: hidden;
    background: var(--backdrop);
  }
  .canvas {
    position: relative;
    width: 1200px;
    height: 987px;
  }
  .card {
    position: absolute;
    left: 75px;
    top: 193px;
    width: 1050px;
    height: 600px;
    background: var(--card);
    box-shadow: 0 2px 10px rgba(0,0,0,0.12);
  }
  .brand {
    position: absolute;
    left: 100px;
    top: 194px;
    width: 420px;
    height: 220px;
    display: flex;
    flex-direction: column;
    justify-content: center;
    align-items: flex-end;
    font-family: "Cinzel", serif;
    font-weight: 600;
    color: var(--ink);
    text-align: right;
  }
  .brand-line {
    display: block;
    font-size: 40px;
    line-height: 1.15;
    letter-spacing: 1px;
  }
  .divider {
    position: absolute;
    left: 546px;
    top: 194px;
    width: 2px;
    height: 220px;
    background: var(--rule);
  }
  .contacts {
    position: absolute;
    left: 582px;
    top: 200px;
  }
  .contact + .contact { margin-top: 16px; }
  .contact-name {
    margin: 0;
    font-family: "Cinzel", serif;
    font-weight: 600;
    font-size: 40px;
    line-height: 46px;
    color: var(--ink);
    letter-spacing: 1px;
  }
  .contact-phone {
    margin: 0;
    font-family: "EB Garamond", serif;
    font-size: 32px;
    line-height: 40px;
    color: var(--phone);
    letter-spacing: 1px;
  }
</style>
</head>
<body>
<main class="canvas">
  <section class="card">
    <div class="brand">
      <span class="brand-line">R &amp; T Summit</span>
      <span class="brand-line">Construction</span>
    </div>
    <div class="divider"></div>
    <div class="contacts">
      <div class="contact">
        <p class="contact-name">Curtis Hale</p>
        <p class="contact-phone">512-693-1804</p>
      </div>
      <div class="contact">
        <p class="contact-name">Nolan Pritchett</p>
        <p class="contact-phone">512-804-2271</p>
      </div>
    </div>
  </section>
</main>
</body>
</html>
```